New business card design

I need original, modern, business looking but dzen (minimalistic) looking design.
Also refer to websit trevanix.ru

Text is

Дробышев Кирилл, PMP
Партнер

Моб. +7 (915) 460 7185
info@trevanix.ru
Москва, Россия, 117342, ул. Береговая 7/2
=====================

Drobyshev Kirill, PMP
Partner

Mob. +7 (915) 460 7185
info@trevanix.ru
Moscow, Russia,117342, Beregovaya 7/2

Industry/Entity Type

Business

Font styles to use
Serif
Sans Serif

```html
<!DOCTYPE html>
<html lang="ru">
<head>
<meta charset="utf-8">
<title>Trevanix — визитная карточка</title>
<link rel="stylesheet" href="https://fonts.googleapis.com/css2?family=Questrial&family=Crimson+Text:wght@400;600&display=swap">
<style>
  :root {
    --backdrop: #e6e7ea;
    --card: #ffffff;
    --brand-blue: #1b7bc2;
    --brand-sky: #6ccdf2;
    --brand-cyan: #2ec1dc;
    --ink: #1e1e1e;
    --name-blue: #2a7fc4;
    --card-shadow: 0 10px 30px rgba(20, 30, 50, 0.18);
  }
  * { box-sizing: border-box; margin: 0; padding: 0; }
  html, body {
    width: 1200px;
    height: 926px;
    overflow: hidden;
    background: var(--backdrop);
  }
  .canvas {
    position: relative;
    width: 1200px;
    height: 926px;
  }
  .card {
    position: absolute;
    left: 220px;
    width: 760px;
    height: 422px;
    background: var(--card);
    box-shadow: var(--card-shadow);
    overflow: hidden;
  }
  .card--front { top: 28px; }
  .card--back { top: 476px; }

  /* Brand lockup */
  .brand {
    position: absolute;
    display: flex;
    align-items: center;
    gap: 18px;
  }
  .brand__mark {
    width: 44px;
    height: 44px;
    background: var(--brand-cyan);
  }
  .brand__name {
    font-family: "Questrial", "Helvetica Neue", Arial, sans-serif;
    color: var(--ink);
    font-weight: 400;
    line-height: 1;
    letter-spacing: 0.5px;
  }
  .card--front .brand {
    left: 50%;
    top: 50%;
    transform: translate(-50%, -50%);
  }
  .card--front .brand__mark { width: 70px; height: 70px; }
  .card--front .brand__name { font-size: 84px; }

  .card--back .brand {
    right: 48px;
    top: 48px;
  }
  .card--back .brand__name { font-size: 54px; }

  /* Side band */
  .band {
    position: absolute;
    left: 0;
    top: 0;
    width: 260px;
    height: 422px;
  }

  /* Person */
  .person {
    position: absolute;
    right: 48px;
    top: 140px;
    text-align: right;
    font-family: "Crimson Text", Georgia, serif;
    color: var(--name-blue);
  }
  .person__name { font-size: 25px; line-height: 1.2; }
  .person__role { font-size: 15px; line-height: 1.2; }

  /* Contacts */
  .contacts {
    position: absolute;
    right: 48px;
    top: 272px;
    list-style: none;
  }
  .contacts__item {
    display: flex;
    justify-content: flex-end;
    align-items: center;
    height: 32px;
  }
  .contacts__text {
    font-family: "Crimson Text", Georgia, serif;
    font-size: 18px;
    color: var(--ink);
    padding-right: 14px;
    white-space: nowrap;
  }
  .contacts__icon {
    width: 62px;
    height: 31px;
    margin-bottom: 1px;
    background: var(--brand-blue);
    display: flex;
    align-items: center;
    justify-content: center;
  }
  .contacts__icon svg { width: 18px; height: 18px; }
</style>
</head>
<body>
<main class="canvas">

  <section class="card card--front" aria-label="Лицевая сторона визитки">
    <div class="brand">
      <span class="brand__mark"></span>
      <span class="brand__name">Trevanix</span>
    </div>
  </section>

  <section class="card card--back" aria-label="Оборотная сторона визитки">
    <svg class="band" viewBox="0 0 260 422" aria-hidden="true">
      <path d="M0 0 H210 C110 70 50 220 70 422 H0 Z" fill="var(--brand-blue)"/>
      <path d="M214 0 H236 C134 80 76 230 96 422 H74 C54 220 114 70 214 0 Z" fill="var(--brand-sky)"/>
    </svg>

    <div class="brand">
      <span class="brand__mark"></span>
      <span class="brand__name">Trevanix</span>
    </div>

    <div class="person">
      <p class="person__name">Дробышев Кирилл,PMP</p>
      <p class="person__role">Партнер</p>
    </div>

    <ul class="contacts">
      <li class="contacts__item">
        <span class="contacts__text">+7 (915) 460 7185</span>
        <span class="contacts__icon">
          <svg viewBox="0 0 24 24" aria-hidden="true"><path fill="#fff" d="M6.6 10.8a15.1 15.1 0 0 0 6.6 6.6l2.2-2.2a1 1 0 0 1 1-.25 11.4 11.4 0 0 0 3.6.57 1 1 0 0 1 1 1V20a1 1 0 0 1-1 1A17 17 0 0 1 3 4a1 1 0 0 1 1-1h3.5a1 1 0 0 1 1 1c0 1.25.2 2.45.57 3.57a1 1 0 0 1-.25 1z"/></svg>
        </span>
      </li>
      <li class="contacts__item">
        <span class="contacts__text">info@trevanix.ru</span>
        <span class="contacts__icon">
          <svg viewBox="0 0 24 24" aria-hidden="true"><rect x="3" y="6" width="18" height="12" fill="none" stroke="#fff" stroke-width="1.8"/><path d="M3 6l9 7 9-7" fill="none" stroke="#fff" stroke-width="1.8"/></svg>
        </span>
      </li>
      <li class="contacts__item">
        <span class="contacts__text">Москва, Россия, 117342, ул. Береговая 7/2</span>
        <span class="contacts__icon">
          <svg viewBox="0 0 24 24" aria-hidden="true"><path fill="#fff" d="M12 3 2 12h3v8h5v-5h4v5h5v-8h3z"/></svg>
        </span>
      </li>
    </ul>
  </section>

</main>
</body>
</html>
```